Realty Group Needs Classy, Contemporary Letterhead Design

We need a letterhead design for a new realty company located in NY, USA. We buy investment properties to rehabilitate and or keep in our rental portfolio.

```html
<!DOCTYPE html>
<html lang="en">
<head>
<meta charset="utf-8">
<title>Northvale Realty Group Letterhead</title>
<link rel="stylesheet" href="https://fonts.googleapis.com/css2?family=Arimo:ital,wght@0,400;0,700;1,400&family=Poppins:wght@500;700&display=swap">
<style>
  :root {
    --brand-purple: #4a2a7e;
    --band-grey: #7d7d7d;
    --ink: #1f1f1f;
    --muted: #6a6a6a;
    --paper: #ffffff;
    --backdrop: #c4c4c4;
  }
  * { box-sizing: border-box; margin: 0; padding: 0; }
  html, body { width: 1200px; height: 1089px; overflow: hidden; }
  body {
    background: var(--backdrop);
    font-family: "Arimo", Arial, sans-serif;
    color: var(--ink);
    position: relative;
  }
  .letterhead {
    position: absolute;
    left: 232px; top: 24px;
    width: 736px; height: 1041px;
    background: var(--paper);
    box-shadow: 0 4px 18px rgba(0,0,0,.18);
    overflow: hidden;
  }
  .brand {
    position: absolute; top: 58px; left: 0; right: 0;
    display: flex; justify-content: center; align-items: center; gap: 10px;
  }
  .brand-dot {
    width: 14px; height: 14px; border-radius: 50%;
    background: var(--brand-purple);
  }
  .brand-name {
    font-family: "Poppins", sans-serif; font-weight: 700;
    font-size: 28px; color: var(--brand-purple); letter-spacing: .5px;
  }
  .brand-rule {
    position: absolute; top: 104px; left: 50%;
    width: 300px; margin-left: -150px; height: 1px;
    background: var(--muted);
  }
  .contact {
    position: absolute; top: 140px; right: 48px;
    list-style: none; font-size: 11px; font-style: italic;
    color: var(--muted); line-height: 1.55;
  }
  .contact li { display: flex; align-items: center; gap: 6px; }
  .contact svg { width: 9px; height: 9px; fill: var(--brand-purple); }
  .letter {
    position: absolute; top: 210px; left: 64px; right: 64px;
    font-size: 13px; line-height: 1.5;
  }
  .date { margin-left: 170px; margin-bottom: 14px; }
  .recipient { margin-left: 90px; margin-bottom: 18px; }
  .recipient strong { font-size: 14px; }
  .salutation { margin-left: 40px; }
  .letter p.body { text-indent: 20px; margin-bottom: 10px; text-align: justify; }
  .closing { margin-top: 4px; }
  .signature {
    width: 110px; height: 26px; margin: 10px 0 4px 20px;
    background: linear-gradient(90deg, #e3e3e3, #f3f3f3);
    border-radius: 4px;
  }
  .sender { font-weight: 700; font-size: 15px; }
  .footer-band {
    position: absolute; left: 0; right: 0; bottom: 0; height: 14px;
    background: var(--band-grey);
  }
  .footer-tab {
    position: absolute; bottom: 0; left: 100px; width: 350px; height: 54px;
    background: var(--brand-purple);
    border-radius: 12px 12px 0 0;
    display: flex; align-items: center; justify-content: center;
    font-family: "Poppins", sans-serif; font-weight: 500;
    font-size: 11px; color: #fff;
  }
</style>
</head>
<body>
  <main class="letterhead">
    <header>
      <div class="brand">
        <span class="brand-dot"></span>
        <span class="brand-name">Northvale Realty Group, LLC</span>
      </div>
      <div class="brand-rule"></div>
      <ul class="contact">
        <li><svg viewBox="0 0 10 10"><path d="M2 1l2 0 1 2-1 1a5 5 0 0 0 2 2l1-1 2 1 0 2-1 1C4 9 1 6 1 2z"/></svg>(555) 014-2290</li>
        <li><svg viewBox="0 0 10 10"><path d="M0 2h10v6H0z M0 2l5 3 5-3" /></svg>info@northvalerealty.com</li>
        <li><svg viewBox="0 0 10 10"><path d="M5 0a3.5 3.5 0 0 1 3.5 3.5C8.5 6 5 10 5 10S1.5 6 1.5 3.5A3.5 3.5 0 0 1 5 0z"/></svg>www.northvalerealty.com</li>
      </ul>
    </header>

    <section class="letter">
      <p class="date">4th September 20XX</p>
      <address class="recipient" style="font-style:normal">
        <strong>Ronny Reader</strong><br>
        CEO, Company Name<br>
        123 Address St<br>
        Anytown, ST 12345
      </address>
      <p class="salutation">Dear Mr. Reader,</p>
      <p class="body">Lorem ipsum dolor sit amet, consectetuer adipiscing elit, sed diam nonummy nibh euismod tincidunt ut laoreet dolore magna aliquam erat volutpat. Ut wisi enim ad minim veniam, quis nostrud exerci tation ullamcorper suscipit lobortis nisl ut aliquip ex ea commodo consequat.</p>
      <p class="body">Duis autem vel eum iriure dolor in hendrerit in vulputate velit esse molestie consequat, vel illum dolore eu feugiat nulla facilisis at vero eros et accumsan.</p>
      <p class="body">Nam liber tempor cum soluta nobis eleifend option congue nihil imperdiet doming id quod mazim placerat facer possim assum. Typi non habent claritatem insitam; est usus legentis in iis qui facit eorum claritatem. Investigationes demonstraverunt lectores legere me lius quod ii legunt saepius.</p>
      <p class="closing">Sincerely,</p>
      <div class="signature" role="img" aria-label="Handwritten signature"></div>
      <p class="sender">Your Name</p>
    </section>

    <footer>
      <div class="footer-band"></div>
      <div class="footer-tab">48 Linden Avenue, Suite 200, Albany, New York 12207</div>
    </footer>
  </main>
</body>
</html>
```